WP website design (Pell)

We need a wordpress design for an established auction and real estate company based in Texas. The winning design will incorporate a professional color scheme with company logo in a clean layout. The design needs to consider that this will be developed on a responsive theme. Colors are those that will highlight the logo.

Reason: was waiting for updated logo

Industry/Entity Type

Real Estate

Font styles to use
Serif
Sans Serif

Requirements
Must have
• Navigation:
1) Home
2) Auctions
3) Online Auctions
4) Services
5) About Us
6) Contact us

Slideshow will be used - please use stock real estate photo. Tag line in the header - "Your Austin Auction Professionals!” Color of the site will be those in the logo and black.

Widgets - 1) Social media icons for twitter, facebook, linkedIn and Rss. 2) News & events blog, 3) Featured video, 4) Email Sign-up, 5) Testimonials

Company logo and contact info in the footer with attached logos too.
Nice to have
• Use of a drop down menu style - under 'Auctions'
1) Upcoming Auctions
2) Past Auctions

```html
<!DOCTYPE html>
<html lang="en">
<head>
<meta charset="utf-8">
<title>Pell Brothers</title>
<link href="https://fonts.googleapis.com/css2?family=Ubuntu:ital,wght@0,400;0,500;0,700;1,400&family=Arimo:wght@400;700&display=swap" rel="stylesheet">
<style>
:root{
  --red:#e3141e;
  --navy:#2b2f8e;
  --navy-dark:#161a5e;
  --black:#0b0b0b;
  --ink:#333;
  --muted:#777;
  --page:#e7e7e7;
  --card:#f7f7f7;
  --white:#fff;
}
*{box-sizing:border-box;margin:0;padding:0}
html,body{width:902px;height:1200px;overflow:hidden}
body{position:relative;background:var(--page);font-family:"Ubuntu",sans-serif;color:var(--ink)}
h1,h2,h3{font-weight:400}
.abs{position:absolute}

/* header */
.top-line{left:0;top:0;width:902px;height:5px;background:var(--red)}
.header{left:0;top:5px;width:902px;height:73px;background:linear-gradient(#fff,#ececec)}
.social{top:12px;width:25px;height:25px;border-radius:50%;background:#8a8f98}
.phone{left:546px;top:53px;font-size:15px;font-weight:700;color:#222;display:flex;align-items:center;gap:4px}
.email{left:689px;top:54px;font-size:13px;color:#222;display:flex;align-items:center;gap:3px}
.nav{left:0;top:78px;width:902px;height:23px;background:var(--navy)}
.nav-item{top:78px;height:23px;line-height:23px;font-size:10.5px;color:#fff;text-transform:uppercase;transform:translateX(-50%)}
.nav-item.active{color:var(--red)}
.nav-sep{top:80px;width:1px;height:19px;background:rgba(255,255,255,.25)}
.brand{left:113px;top:5px;width:151px;height:73px;background:#fff;display:flex;align-items:center;justify-content:center;gap:7px}
.brand-mark{width:10px;height:10px;background:var(--red)}
.brand-name{font-size:20px;font-weight:500;color:var(--black)}
.dropdown{left:352px;top:101px;width:132px;height:77px;background:rgba(43,47,142,.92);border-bottom:5px solid var(--red);z-index:3}
.dropdown li{list-style:none;font-size:10.5px;color:#fff;text-transform:uppercase;padding-left:14px;height:33px;line-height:42px}

/* slider */
.slider-bg{left:0;top:101px;width:902px;height:242px;background:linear-gradient(90deg,#7f9a3a,#b9c97a 8%,#cfd5c2 12%,#cfd5c2 88%,#b9c97a 92%,#7f9a3a)}
.slide{left:102px;top:101px;width:698px;height:242px;background:linear-gradient(#c9d6e3 0%,#d8d4c8 35%,#a9927a 70%,#4b5a32 100%)}
.tagline{left:102px;top:204px;width:698px;text-align:center;font-size:31px;font-weight:500;color:#fff;text-shadow:2px 2px 0 #c0141b;letter-spacing:-.5px}
.slide-arrow{top:208px;width:32px;height:32px;border-radius:50%;background:rgba(255,255,255,.75)}
.dot{top:325px;width:13px;height:11px;background:#ddd;border:1px solid #999}

/* main */
.welcome{left:102px;top:362px;font-size:23px;color:var(--red)}
.intro{left:102px;top:399px;width:482px;font-size:10.5px;line-height:14.5px;color:#666}
.section-title{left:101px;top:488px;font-size:21px;color:var(--black)}
.title-rule{left:242px;top:499px;width:340px;height:7px;border-top:2px solid var(--red);border-bottom:2px solid var(--red)}
.card{left:102px;width:480px;height:188px;background:var(--card);box-shadow:0 0 2px #ccc}
.card-photo{position:absolute;left:8px;top:8px;width:221px;height:112px;background:linear-gradient(#b9cde2 0%,#c7c9c2 35%,#9a6a52 60%,#6e8f45 85%,#5b7d3a 100%)}
.btn{position:absolute;width:95px;height:23px;background:var(--red);color:#fff;font-family:"Arimo",sans-serif;font-size:12px;display:flex;align-items:center;justify-content:center;gap:5px;border:1px solid #b50d15}
.btn i{display:inline-block;width:12px;height:11px;background:#f1d45a;border-radius:2px}
.card-title{position:absolute;left:241px;top:6px;font-size:16px;color:var(--red)}
.card-sub{position:absolute;left:241px;top:24px;width:220px;font-size:9.5px;line-height:12px;color:#777}
.mode{position:absolute;left:241px;font-size:12.5px;color:#444;letter-spacing:.3px}
.row{position:absolute;left:241px;font-family:"Arimo",sans-serif;font-size:10px;color:#333;display:flex}
.row b{font-weight:400;color:#555;width:52px}
.row span{width:175px;line-height:12px}
.page-box{top:912px;width:17px;height:17px;background:#8e8e8e;color:#fff;font-size:11px;text-align:center;line-height:17px}
.signup{left:102px;top:944px;width:480px;height:53px;background:#8c8c8c}
.signup-text{left:102px;top:944px;width:204px;height:53px;background:var(--red);clip-path:polygon(0 0,186px 0,100% 50%,186px 100%,0 100%);color:#fff;font-family:"Arimo",sans-serif;font-size:9.8px;line-height:13px;padding:14px 0 0 9px}
.signup-input{left:314px;top:957px;width:177px;height:28px;background:#999;border:1px solid #b5b5b5;color:#ddd;font-family:"Arimo",sans-serif;font-size:8.5px;line-height:26px;padding-left:8px}
.signup-btn{left:497px;top:957px;width:78px;height:28px;background:var(--red);color:#fff;font-size:12.5px;text-align:center;line-height:28px}

/* sidebar */
.widget{left:596px;width:202px;background:#f8f8f8;box-shadow:0 0 2px #bbb}
.widget-head{left:596px;width:202px;height:32px;background:var(--black);color:#fff;text-align:center;font-size:18px;line-height:32px}
.video{left:603px;top:409px;width:189px;height:139px;background:linear-gradient(135deg,#f0f0f0,#c9cfd2 60%,#8d9a8a);border:1px solid #aaa}
.play{left:673px;top:455px;width:47px;height:33px;border-radius:8px;background:#222}
.date{left:604px;width:54px;height:53px;background:var(--red);color:#fff;text-align:center;font-size:22px;line-height:24px;padding-top:3px}
.date small{display:block;font-size:17px}
.news-text{left:665px;width:126px;font-size:9.5px;line-height:11.5px;color:#555}
.more{font-size:8.5px;color:var(--red);display:block;margin-top:3px}
.news-rule{left:604px;top:740px;width:183px;height:3px;background:var(--red)}
.view-all{left:670px;top:749px;font-size:10px;color:var(--red)}
.quote{left:621px;top:835px;width:165px;font-size:9.5px;line-height:12.5px;font-style:italic;color:#666}
.qmark{font-size:38px;color:#ccc;font-family:Georgia,serif}
.author{left:706px;top:938px;font-size:13px;color:var(--red)}
.tdot{top:977px;width:8px;height:8px;background:#444}

/* footer */
.footer{left:0;top:1013px;width:902px;height:162px;background:#d6d6d6;border-top:2px solid #fff}
.foot-brand{left:150px;top:1090px;width:140px;display:flex;align-items:center;justify-content:center;gap:7px}
.vline{top:1055px;width:1px;height:100px;background:#aaa}
.badge-sq{left:390px;top:1050px;width:63px;height:70px;background:#1b1b1b}
.badge-round{left:491px;top:1052px;width:60px;height:60px;border-radius:50%;background:#c8a04a;border:3px solid #6b4f1c}
.badge-wide{left:378px;top:1132px;width:172px;height:34px;background:#f28a1c}
.contact-title{left:622px;top:1019px;font-size:20px;color:var(--red)}
.contact-name{left:622px;top:1050px;font-size:12.5px;color:#222}
.contact-line{left:622px;font-size:10px;color:#333;display:flex;align-items:center;gap:6px}
.bottom-bar{left:0;top:1175px;width:902px;height:25px;background:var(--navy-dark);color:#ddd;font-family:"Arimo",sans-serif;font-size:8.5px;text-align:center;line-height:25px}
</style>
</head>
<body>

<div class="abs top-line"></div>
<header class="abs header"></header>
<div class="abs social" style="left:680px"></div>
<div class="abs social" style="left:712px"></div>
<div class="abs social" style="left:744px"></div>
<div class="abs social" style="left:775px"></div>
<div class="abs phone"><svg width="16" height="16" viewBox="0 0 24 24"><path d="M6.6 10.8a15 15 0 006.6 6.6l2.2-2.2c.3-.3.7-.4 1-.2 1.1.4 2.3.6 3.6.6.6 0 1 .4 1 1V20c0 .6-.4 1-1 1A17 17 0 013 4c0-.6.4-1 1-1h3.5c.6 0 1 .4 1 1 0 1.3.2 2.5.6 3.6.1.3 0 .7-.2 1z" fill="#222"/></svg>(512) 555-0148</div>
<div class="abs email"><svg width="14" height="10" viewBox="0 0 14 10"><rect x=".5" y=".5" width="13" height="9" fill="none" stroke="#222"/><path d="M.5.5l6.5 5 6.5-5" fill="none" stroke="#222"/></svg>info@pellbas.com</div>

<nav class="abs nav"></nav>
<div class="abs nav-item" style="left:320px">Home</div>
<div class="abs nav-sep" style="left:352px"></div>
<div class="abs nav-item active" style="left:393px">Auctions</div>
<div class="abs nav-sep" style="left:435px"></div>
<div class="abs nav-item" style="left:493px">Online Auctions</div>
<div class="abs nav-sep" style="left:553px"></div>
<div class="abs nav-item" style="left:592px">Services</div>
<div class="abs nav-sep" style="left:633px"></div>
<div class="abs nav-item" style="left:672px">About Us</div>
<div class="abs nav-sep" style="left:713px"></div>
<div class="abs nav-item" style="left:759px">Contact Us</div>

<div class="abs brand"><span class="brand-mark"></span><span class="brand-name">Pell Brothers</span></div>

<div class="abs slider-bg"></div>
<div class="abs slide" role="img" aria-label="Photo of a suburban house at dusk with an auction sign on the lawn"></div>
<ul class="abs dropdown"><li>- Upcoming Auctions</li><li>- Past Auctions</li></ul>
<div class="abs tagline">Your Austin Auction Professionals!</div>
<div class="abs slide-arrow" style="left:112px"><svg width="32" height="32"><path d="M19 9l-7 7 7 7" stroke="#555" stroke-width="2.5" fill="none"/></svg></div>
<div class="abs slide-arrow" style="left:758px"><svg width="32" height="32"><path d="M13 9l7 7-7 7" stroke="#555" stroke-width="2.5" fill="none"/></svg></div>
<div class="abs dot" style="left:437px"></div>
<div class="abs dot" style="left:453px"></div>
<div class="abs dot" style="left:469px"></div>

<h1 class="abs welcome">Welcome to Pell Brothers Action Services</h1>
<p class="abs intro">Lorem Ipsum. Proin gravida nibh vel velit auctor aliquet. Aenean sollicitudin, lorem quis bibendum auctor, nisi elit consequat ipsum, nec sagittis sem nibh id elit. Duis sed odio sit amet nibh vulputate cursus a sit amet mauris. Morbi accumsan ipsum velit. Nam nec tellus a odio tincidunt auctor a ornare odio. Sed non&nbsp; mauris vitae erat consequat auctor eu in elit. Class aptent taciti sociosqu ad litora torquent per conubia nostra...</p>

<h2 class="abs section-title">Current Action</h2>
<div class="abs title-rule"></div>

<article class="abs card" style="top:516px">
  <div class="card-photo" role="img" aria-label="Photo of a large brick family home with a lawn"></div>
  <div class="btn" style="left:19px;top:126px"><i></i>Details</div>
  <div class="btn" style="left:122px;top:126px"><i></i>Photos</div>
  <div class="btn" style="left:19px;top:155px"><i style="background:#9bc53d"></i>Video</div>
  <div class="btn" style="left:122px;top:155px"><i style="background:#7fb0e0"></i>Online Now!</div>
  <h3 class="card-title">Lorem Ipsum proin gravida nib</h3>
  <p class="card-sub">Lorem Ipsum. Proin gravida nibh vel velit auctor aliquet. Aenean sollicitudin,</p>
  <div class="mode" style="top:54px">Online Bidding Only</div>
  <div class="row" style="top:72px"><b>Begins:</b><span>Monday, June 26, 2014 at 4:00 PM</span></div>
  <div class="row" style="top:86px"><b>End:</b><span>Tuesday, June 27, 2014 at 4:00 PM</span></div>
  <div class="mode" style="top:108px">Live Off-Site Auction</div>
  <div class="row" style="top:127px"><b>Begins:</b><span>Monday, June 26, 2014 at 4:00 PM</span></div>
  <div class="row" style="top:142px"><b>End:</b><span>Tuesday, June 27, 2014 at 4:00 PM</span></div>
  <div class="row" style="top:158px"><b>Location:</b><span>Lorem Ipsum. Proin gravida nibh vel velit auctor aliquet Aenean sollicitudin,</span></div>
</article>

<article class="abs card" style="top:719px">
  <div class="card-photo" role="img" aria-label="Photo of a large brick family home with a lawn"></div>
  <div class="btn" style="left:19px;top:126px"><i></i>Details</div>
  <div class="btn" style="left:122px;top:126px"><i></i>Photos</div>
  <div class="btn" style="left:19px;top:155px"><i style="background:#9bc53d"></i>Video</div>
  <div class="btn" style="left:122px;top:155px"><i style="background:#7fb0e0"></i>Online Now!</div>
  <h3 class="card-title">Lorem Ipsum proin gravida nib</h3>
  <p class="card-sub">Lorem Ipsum. Proin gravida nibh vel velit auctor aliquet. Aenean sollicitudin.</p>
  <div class="mode" style="top:54px">Online Bidding Only</div>
  <div class="row" style="top:72px"><b>Begins:</b><span>Monday, June 26, 2014 at 4:00 PM</span></div>
  <div class="row" style="top:86px"><b>End:</b><span>Tuesday, June 27, 2014 at 4:00 PM</span></div>
  <div class="mode" style="top:108px">Live Off-Site Auction</div>
  <div class="row" style="top:127px"><b>Begins:</b><span>Monday, June 26, 2014 at 4:00 PM</span></div>
  <div class="row" style="top:142px"><b>End:</b><span>Tuesday, June 27, 2014 at 4:00 PM</span></div>
  <div class="row" style="top:158px"><b>Location:</b><span></span></div>
</article>

<div class="abs page-box" style="left:507px">1</div>
<div class="abs page-box" style="left:525px">2</div>
<div class="abs page-box" style="left:544px">3</div>
<div class="abs page-box" style="left:563px">4</div>

<div class="abs signup"></div>
<div class="abs signup-text">To stay informed about our services and upcoming events, please join our mailing</div>
<div class="abs signup-input">Enter Your Email Address...</div>
<div class="abs signup-btn">Subscribe</div>

<div class="abs widget" style="top:366px;height:194px"></div>
<div class="abs widget-head" style="top:366px">Featured video</div>
<div class="abs video" role="img" aria-label="Video still of a white villa with balconies and flowers"></div>
<div class="abs play"><svg width="47" height="33"><path d="M19 10l11 6.5-11 6.5z" fill="#fff"/></svg></div>

<div class="abs widget" style="top:575px;height:193px"></div>
<div class="abs widget-head" style="top:575px">News &amp; Events</div>
<div class="abs date" style="top:615px">15<small>June</small></div>
<div class="abs news-text" style="top:614px">Lorem Ipsum. Proin gravida nibh vel velit auctor aliquet. Aenean sollicitudin, lorem<span class="more">Learn more⟶</span></div>
<div class="abs date" style="top:682px">15<small>June</small></div>
<div class="abs news-text" style="top:682px">Lorem Ipsum. Proin gravida nibh vel velit auctor aliquet. Aenean sollicitudin, lorem<span class="more">Learn more⟶</span></div>
<div class="abs news-rule"></div>
<div class="abs view-all">View All <svg width="14" height="10" viewBox="0 0 14 10"><path d="M0 5h12M8 1l4 4-4 4" stroke="#333" stroke-width="1.5" fill="none"/></svg></div>

<div class="abs widget" style="top:782px;height:213px"></div>
<div class="abs widget-head" style="top:782px">Testimonials</div>
<div class="abs qmark" style="left:599px;top:818px">“</div>
<p class="abs quote">Lorem Ipsum. Proin gravida nibh vel velit auctor aliquet. Aenean sollicitudin, lorem quis bibendum auctor, nisi elit consequat ipsum, nec sagittis sem nibh id elit. Duis sed odio sit amet nibh vulputate cursus a sit amet mauris...</p>
<div class="abs qmark" style="left:748px;top:900px">”</div>
<div class="abs author">- Mara, Texas</div>
<div class="abs tdot" style="left:681px;background:var(--red)"></div>
<div class="abs tdot" style="left:691px"></div>
<div class="abs tdot" style="left:701px"></div>
<div class="abs tdot" style="left:711px"></div>

<footer class="abs footer"></footer>
<div class="abs foot-brand"><span class="brand-mark"></span><span class="brand-name">Pell Brothers</span></div>
<div class="abs vline" style="left:336px"></div>
<div class="abs badge-sq" role="img" aria-label="Partner association badge"></div>
<div class="abs badge-round" role="img" aria-label="State auctioneers association seal"></div>
<div class="abs badge-wide" role="img" aria-label="University partner badge"></div>
<div class="abs vline" style="left:594px"></div>
<h3 class="abs contact-title">Contact info</h3>
<div class="abs contact-name">Pell Brothers Action Services</div>
<div class="abs contact-line" style="top:1073px"><svg width="10" height="13" viewBox="0 0 10 13"><path d="M5 12S1 7 1 4.5a4 4 0 018 0C9 7 5 12 5 12z" fill="none" stroke="#333" stroke-width="1.3"/><circle cx="5" cy="4.5" r="1.4" fill="#333"/></svg>Lorem Ipsum proin gravida nibh</div>
<div class="abs contact-line" style="top:1097px"><svg width="11" height="11" viewBox="0 0 11 11"><path d="M1 5l4.5-4 4.5 4v5H1z" fill="none" stroke="#333" stroke-width="1.3"/></svg>Gravida nibhLorem Ipsum proin</div>
<div class="abs contact-line" style="top:1117px"><svg width="11" height="9" viewBox="0 0 11 9"><rect x="1" y="3" width="9" height="5" fill="#333"/><rect x="0" y="0" width="11" height="3" rx="1.5" fill="#333"/></svg>(512) 555-0148</div>
<div class="abs contact-line" style="top:1134px"><svg width="11" height="10" viewBox="0 0 11 10"><rect x="0" y="3" width="11" height="5" fill="#333"/><rect x="2" y="0" width="7" height="3" fill="#333"/><rect x="2" y="7" width="7" height="3" fill="#fff" stroke="#333"/></svg>(512) 555-0149</div>
<div class="abs contact-line" style="top:1152px"><svg width="12" height="9" viewBox="0 0 12 9"><rect x=".5" y=".5" width="11" height="8" fill="none" stroke="#333"/><path d="M.5.5l5.5 4.5 5.5-4.5" fill="none" stroke="#333"/></svg>info@pellbas.com</div>
<div class="abs bottom-bar">(c) 2014. Pell Brothers Action Services | All Rights Reserved.</div>

</body>
</html>
```